Motel Flyer to Attract Regular Business Clients

Using our existing logo (Wattlecrest Motel) and some excellent photos we seek a modern and effective marketing tool in this DL brochure. It aims to attract ongoing contracts with businesses employing or contracting mobile staff, such as product rep's, project workers and truck drivers, so that there is always a room available for the personnel with home comforts, such as laundry service, pick ups, parking etc

If you are looking at the business card, I have mistakenly put this on another job. I do have another brief needing a card, so the details and logo will be different. Joy Added Thursday, December 17, 2015

Target Market(s)

Trucking Companies
Regional servicing companies - mechanical, electrical
Civil Construction
Project management companies

Industry/Entity Type

Motel

Contact Information for Business Card

Logo - Kestrel Skyfield
Rebecca McArdle
M
P 07 4918 3273
F 07 4918 3275

PO Box 562 St George Qld 4487
E rebecca@kestrelskyfield.example

Font styles to use
Sans Serif

Colors
0555a3
0393ce
00a990
9ccb3b

Requirements
Must have
• DL sized flyer
• Century Gothic font
• Salt Water Pool and Slide
• Quiet Location
• Well Known Restaurant
• 24/7 Check-in times
• Free Wi-Fi
• Air-conditioning
Nice to have
• DL Flyer:
• We have created a home away from home for personnel travelling through Brolga Creek.
• Trucking companies and many product sales reps choose Wattlecrest Motel for ongoing and regular stay-overs.
• Please call Martin or Nicole on (07) 4839 2207 to discuss packages for your mobile teams, so we can have a bed ready for you any time.

```html
<!DOCTYPE html>
<html lang="en">
<head>
<meta charset="utf-8">
<title>Wattlecrest Motel – DL Flyers</title>
<link rel="stylesheet" href="https://fonts.googleapis.com/css2?family=Montserrat:wght@700;800&family=Questrial&display=swap">
<style>
  :root {
    --blue: #0a4aa0;
    --blue-deep: #083f8c;
    --green: #2aa836;
    --green-bright: #3cb44a;
    --ink: #111111;
    --white: #ffffff;
    --backdrop: #ecebe8;
    --photo-garden-a: #3d4a2c;
    --photo-garden-b: #7a6a4e;
    --photo-dusk-a: #d98a7a;
    --photo-dusk-b: #2b2424;
    --photo-room-a: #9a5a3a;
    --photo-room-b: #4a3a30;
    --photo-owners-a: #6a88b0;
    --photo-owners-b: #d8d8da;
  }
  * { box-sizing: border-box; margin: 0; padding: 0; }
  html, body { width: 1200px; height: 900px; overflow: hidden; }
  body { background: var(--backdrop); font-family: "Questrial", "Century Gothic", sans-serif; position: relative; }

  .flyer { position: absolute; background: var(--white); overflow: hidden; box-shadow: 0 4px 14px rgba(0,0,0,.18); }
  .flyer--garden { left: 158px; top: 65px; width: 370px; height: 765px; }
  .flyer--pool { left: 672px; top: 70px; width: 366px; height: 752px; }

  .headline { position: absolute; left: 0; right: 0; top: 26px; text-align: center;
    font-family: "Montserrat", "Century Gothic", sans-serif; font-weight: 800; line-height: 1; z-index: 3; }
  .headline__top { display: block; font-size: 24px; }
  .headline__bottom { display: block; font-size: 33px; margin-top: 6px; }
  .flyer--garden .headline__top { color: var(--ink); }
  .flyer--garden .headline__bottom { color: var(--blue); }
  .flyer--pool .headline__top { color: var(--blue); }
  .flyer--pool .headline__bottom { color: var(--green); }

  .photo { position: absolute; left: 0; right: 0; }
  .photo--garden { top: 110px; height: 340px; background: linear-gradient(160deg, var(--photo-garden-a), var(--photo-garden-b) 60%, var(--photo-garden-a)); }
  .photo--dusk { top: 110px; height: 250px; background: linear-gradient(180deg, var(--photo-dusk-a), #b06a60 35%, var(--photo-dusk-b) 75%); }

  .shapes { position: absolute; inset: 0; width: 100%; height: 100%; z-index: 1; }

  .portrait { position: absolute; border-radius: 50%; z-index: 2; }
  .portrait--room { left: 42px; top: 338px; width: 144px; height: 144px;
    border: 6px solid var(--green); box-shadow: 0 0 0 5px var(--blue);
    background: linear-gradient(135deg, var(--photo-room-a), var(--photo-room-b)); }
  .portrait--owners { left: 229px; top: 343px; width: 124px; height: 124px;
    border: 5px solid var(--green-bright); box-shadow: 0 0 0 5px var(--blue);
    background: linear-gradient(180deg, var(--photo-owners-b), var(--photo-owners-a)); }

  .brand { position: absolute; z-index: 2; text-align: center; }
  .brand__mark { display: block; width: 34px; height: 34px; margin: 0 auto 6px; border-radius: 50%; }
  .brand__name { display: block; font-size: 19px; line-height: 1; }
  .brand__sub { display: block; font-size: 8px; margin-top: 2px; letter-spacing: .3px; }
  .flyer--garden .brand { left: 200px; top: 396px; width: 140px; color: var(--white); }
  .flyer--garden .brand__mark { background: var(--white); }
  .flyer--pool .brand { left: 213px; top: 522px; width: 140px; color: var(--blue); }
  .flyer--pool .brand__mark { background: var(--blue); }

  .blurb { position: absolute; z-index: 2; line-height: 1.25; text-align: justify; }
  .flyer--garden .blurb { left: 33px; width: 311px; top: 503px; color: var(--white); font-size: 15px; }
  .flyer--pool .blurb { left: 29px; width: 230px; top: 474px; color: var(--ink); font-size: 13.5px; }

  .call { position: absolute; z-index: 2; }
  .call__label { display: block; font-size: 12.5px; }
  .call__phone { display: block; font-family: "Montserrat", "Century Gothic", sans-serif; font-weight: 700; font-size: 21px; margin-top: 6px; }
  .flyer--garden .call { left: 33px; top: 570px; color: var(--white); }
  .flyer--garden .call__phone { color: var(--green-bright); }
  .flyer--pool .call { left: 30px; top: 630px; color: var(--white); }
  .flyer--pool .call__label { padding-left: 32px; }
  .call__note { display: block; font-size: 12px; line-height: 1.25; margin-top: 12px; width: 295px; }

  .address-panel { position: absolute; left: 18px; top: 628px; width: 338px; height: 118px;
    background: var(--white); border-radius: 22px; z-index: 2; }

  .features { position: absolute; left: 30px; top: 364px; list-style: none; z-index: 2; }
  .features li { font-size: 13.5px; line-height: 16.8px; color: var(--ink); position: relative; padding-left: 16px; }
  .features li::before { content: ""; position: absolute; left: 0; top: 5px; width: 7px; height: 7px; border-radius: 50%; background: var(--blue); }
</style>
</head>
<body>

<section class="flyer flyer--garden">
  <h1 class="headline"><span class="headline__top">COUNTRY HOSPITALITY</span><span class="headline__bottom">FOR TRAVELLERS</span></h1>
  <div class="photo photo--garden" role="img" aria-label="Motel garden courtyard with palms, outdoor kitchen hut and barbecue area"></div>
  <svg class="shapes" viewBox="0 0 370 765" preserveAspectRatio="none" aria-hidden="true">
    <path d="M0 0 H370 V100 C300 108 230 150 130 152 C70 153 30 145 0 138 Z" fill="var(--white)"/>
    <path d="M0 138 C30 145 70 153 130 152 C230 150 300 108 370 100 V112 C300 122 230 162 130 164 C70 165 30 156 0 150 Z" fill="var(--green)"/>
    <path d="M0 415 C110 435 230 380 370 345 V765 H0 Z" fill="var(--white)"/>
    <path d="M0 428 C110 448 230 392 370 358 V765 H0 Z" fill="var(--blue)"/>
  </svg>
  <div class="portrait portrait--room" role="img" aria-label="Motel guest room with a made bed"></div>
  <div class="brand"><span class="brand__mark"></span><span class="brand__name">Wattlecrest</span><span class="brand__sub">Motel &amp; Saltbush Restaurant</span></div>
  <p class="blurb">Trucking companies and many product sales reps choose Wattlecrest Motel for ongoing and regular stay-overs.</p>
  <p class="call"><span class="call__label">PLEASE CALL ON</span><span class="call__phone">(07) 4839 2207</span></p>
  <div class="address-panel"></div>
</section>

<section class="flyer flyer--pool">
  <h1 class="headline"><span class="headline__top">COUNTRY HOSPITALITY</span><span class="headline__bottom">FOR TRAVELLERS</span></h1>
  <div class="photo photo--dusk" role="img" aria-label="Salt water pool and slide under palm trees at sunset"></div>
  <svg class="shapes" viewBox="0 0 366 752" preserveAspectRatio="none" aria-hidden="true">
    <path d="M0 0 H366 V100 C260 100 160 112 80 128 C45 135 20 130 0 118 Z" fill="var(--white)"/>
    <path d="M0 92 C20 110 45 118 80 112 C160 98 260 100 366 100 V108 C260 110 160 126 80 146 C45 154 20 150 0 140 Z" fill="var(--blue)"/>
    <path d="M0 345 C90 320 180 310 270 330 C310 338 340 346 366 346 V752 H0 Z" fill="var(--green)"/>
    <path d="M0 356 C90 334 180 326 270 344 C310 352 340 358 366 358 V752 H0 Z" fill="var(--white)"/>
    <path d="M0 612 C60 590 120 572 180 572 C260 572 320 600 366 620 V752 H0 Z" fill="var(--green)"/>
    <path d="M0 622 C60 600 120 584 180 584 C260 584 320 612 366 632 V752 H0 Z" fill="var(--blue)"/>
  </svg>
  <ul class="features">
    <li>Free Wi-Fi</li>
    <li>Quiet Location</li>
    <li>Air-conditioning</li>
    <li>Well Known Restaurant</li>
    <li>Salt Water Pool and Slide</li>
    <li>24/7 Check-in times</li>
  </ul>
  <div class="portrait portrait--owners" role="img" aria-label="Photo of the motel hosts"></div>
  <p class="blurb">We have created a home away from home for personnel travelling through Brolga Creek.</p>
  <div class="brand"><span class="brand__mark"></span><span class="brand__name">Wattlecrest</span><span class="brand__sub">Motel &amp; Saltbush Restaurant</span></div>
  <p class="call"><span class="call__label">PLEASE CALL ON</span><span class="call__phone">(07) 4839 2207</span><span class="call__note">to discuss packages for your mobile teams, so we can have a bed ready for you any time.</span></p>
</section>

</body>
</html>
```